依頼詳細
親しみやすいロゴですが、大企業にも恥じないスタイリッシュなデザインを求めています。
お客様に不信感を与えず、信頼を得やすいデザインを求めています。
また、IT系の企業なので、未来のあるデザインが良いです。
一度もらったら忘れないデザインなど、最高です!
私たちでは思いつかない部分が多いので、素晴らしいデザインをご提案下さいませ。

依頼詳細
・両面でお願いします。
・裏面には事業内容を列挙できるようなものがよいです。
記載項目を挙げていますが、○で埋めて頂いて結構です。
例)〒○○○-○○○○
記載項目
表面:ロゴ、役職、名前(ローマ字付)、会社名、郵便番号、住所、TEL、FAX、MAIL
裏面:事業内容
希望イメージ
シンプル 複雑
単色 カラフル
暗い 明るい
日常 高級
遊び心 厳粛
未来的 伝統的
女性的 男性的
希望する色
緑系、グレー系
納品ファイル
• イラストレーター形式 (.ai)
補足説明
文字をこちらで入力するので、
名前や住所、事業内容の部分はmacやwindowsで使用できるフォントを使って下さい。
名刺サイズについて
55 × 91 ミリ
縦、横問いません。
aiデータを添付します。
奇抜なアイディアを是非お待ちしております。
大企業に恥じないとは言いますが、
目にとまる、遊び心があっても良いと思っています。
インパクトのある名刺を是非宜しくお願い致します。
※募集期間を延長します。
さまざまなアイディアを募集しております。
実際の使用例、レーザー抜、箔押し、エンボス、デボスなど、
創意工夫の点をアドバイス頂けると評価が高いです。
宜しくお願い致します。
説明が不足しておりました。
印刷は、弊社がプリントサービス等にデータ入稿致します。
先ほど追記した加工は、提案でかまいません。
クリエル様には、あくまでもデータだけの提出をお願いしております。

わかりづらい点が多いですが、
ご質問いただければすぐ回答するように致します。

宜しくお願い致します。
■ 選んだ理由

当選のデザインですが、弊社の主力業務であるソフトウェアの中でも、得意としている分野をアピールしてくれるデザインでした。
私たちが言わなくとも、弊社の業務をお調べしていただき、デザインにしていただけたのが嬉しかったです。
印刷方法までご提示頂けたので、とても助かりました。

■ 提案者全員のお礼・コメント

この度は貴重なお時間をいただき、
弊社のデザインをご提案下さいまして誠にありがとうございます。
また機会がありましたら、是非とも宜しくお願い致します。

```html
<!DOCTYPE html>
<html lang="ja">
<head>
<meta charset="utf-8">
<title>Nexa Grid Labs 名刺デザイン</title>
<link href="https://fonts.googleapis.com/css2?family=Noto+Sans+JP:wght@400;500;700&display=swap" rel="stylesheet">
<style>
  :root{
    --green:#6aae2a;
    --green-soft:#8cc63f;
    --ink:#333333;
    --grey:#6e6e6e;
    --grey-light:#9a9a9a;
    --sheet:#ffffff;
    --card:#ffffff;
    --deco:#f1f1f1;
    --band:#4a4a4a;
  }
  *{margin:0;padding:0;box-sizing:border-box}
  html,body{width:900px;height:1200px;overflow:hidden;background:var(--sheet)}
  body{position:relative;font-family:"Noto Sans JP",sans-serif;color:var(--ink)}
  .side-label{position:absolute;right:52px;font-size:15px;color:var(--grey);letter-spacing:.02em}
  .side-label--front{top:22px}
  .side-label--back{top:598px}
  .card{position:absolute;left:60px;width:789px;height:477px;background:var(--card);
        box-shadow:0 2px 8px rgba(0,0,0,.25);overflow:hidden}
  .card--front{top:54px}
  .card--back{top:630px}
  .card__deco{position:absolute;background:linear-gradient(180deg,var(--deco),#f7f7f7)}
  .card--front .card__deco{left:360px;top:150px;width:429px;height:327px}
  .card--back .card__deco{left:0;top:0;width:789px;height:477px;opacity:.7}
  .brand{position:absolute;display:flex;align-items:center;gap:14px}
  .brand__dot{width:54px;height:54px;border-radius:50%;background:var(--green)}
  .brand__name{font-weight:700;color:var(--grey);white-space:nowrap}
  .card--front .brand{left:30px;top:30px}
  .card--front .brand__name{font-size:46px;letter-spacing:-.01em}
  .person{position:absolute;left:21px;top:138px}
  .person__title{font-size:15px;color:var(--ink)}
  .person__name{font-size:38px;font-weight:500;letter-spacing:.25em;margin-top:4px;line-height:1.2}
  .person__roman{font-size:13px;color:var(--grey);margin-top:8px;letter-spacing:.05em}
  .contact{position:absolute;left:468px;top:180px;list-style:none}
  .contact li{display:flex;align-items:center;gap:10px;font-size:20px;height:42px;color:var(--ink)}
  .contact svg{width:22px;height:22px;flex:none}
  .company{position:absolute;left:21px;top:292px}
  .company__name{font-size:24px;font-weight:500;color:var(--green)}
  .company__address{font-size:16px;margin-top:8px;color:var(--ink)}
  .card--back .brand{left:0;right:0;top:58px;flex-direction:column;gap:8px}
  .card--back .brand__dot{width:60px;height:60px}
  .card--back .brand__name{font-size:26px}
  .services{position:absolute;left:0;right:0;top:218px;text-align:center;font-size:17px;line-height:28px;color:var(--ink)}
  .services__heading{margin-bottom:2px}
  .services ul{list-style:none}
  .footer-band{position:absolute;left:0;bottom:0;width:900px;height:44px;background:var(--band)}
</style>
</head>
<body>
  <p class="side-label side-label--front">design001：おもて面</p>
  <section class="card card--front">
    <div class="card__deco" role="img" aria-label="淡いグレーの大きな装飾シンボル"></div>
    <div class="brand">
      <span class="brand__dot"></span>
      <span class="brand__name">Nexa Grid Labs</span>
    </div>
    <div class="person">
      <p class="person__title">代表取締役</p>
      <p class="person__name">クリエル 健</p>
      <p class="person__roman">Ken Crier</p>
    </div>
    <ul class="contact">
      <li><svg viewBox="0 0 22 22"><circle cx="11" cy="11" r="11" fill="var(--green-soft)"/><path d="M7 6.5c.6-.6 1.4-.5 1.8.1l1 1.5c.3.5.2 1-.2 1.4l-.6.5c.5 1.2 1.4 2.1 2.6 2.6l.5-.6c.4-.4.9-.5 1.4-.2l1.5 1c.6.4.7 1.2.1 1.8l-.6.6c-2.8 1-8.3-4.5-7.3-7.3z" fill="#fff"/></svg>03-5550-0142</li>
      <li><svg viewBox="0 0 22 22"><circle cx="11" cy="11" r="11" fill="var(--green-soft)"/><rect x="6" y="9" width="10" height="6" rx="1" fill="#fff"/><rect x="8" y="6" width="6" height="3" fill="#fff"/></svg>03-5550-0143</li>
      <li><svg viewBox="0 0 22 22"><circle cx="11" cy="11" r="11" fill="var(--green-soft)"/><rect x="6" y="7.5" width="10" height="7" rx="1" fill="#fff"/><path d="M6.5 8l4.5 3.5L15.5 8" stroke="var(--green-soft)" stroke-width="1" fill="none"/></svg>k.crier@nexagrid.jp</li>
    </ul>
    <div class="company">
      <p class="company__name">株式会社 ネクサグリッドラボ</p>
      <p class="company__address">〒104-0000 東京都港区青葉2丁目8-16 グリッドビル4F</p>
    </div>
  </section>

  <p class="side-label side-label--back">design001：うら面</p>
  <section class="card card--back">
    <div class="card__deco" role="img" aria-label="淡いグレーの大きな装飾シンボルの連続"></div>
    <div class="brand">
      <span class="brand__dot"></span>
      <span class="brand__name">Nexa Grid Labs</span>
    </div>
    <div class="services">
      <p class="services__heading">事業内容</p>
      <ul>
        <li>ネットワーク管理システム開発</li>
        <li>〇〇〇システム開発</li>
        <li>〇〇管理システム開発</li>
        <li>〇〇〇〇〇〇システム開発</li>
        <li>〇〇〇〇システム開発</li>
        <li>〇〇〇〇〇システム開発</li>
        <li>〇〇システム開発</li>
      </ul>
    </div>
  </section>

  <div class="footer-band"></div>
</body>
</html>
```